Brivenor Australia Company Values.

We have just completed our company purpose, beliefs and values (for the first time, we have not had these before)
We are now wanting to add images to each company value as a visual
so they are easily identified and understood for all our staff - we need them to remember the 5 Values.
We are a manufacturer of dental materials and infection control products, based in Melbourne.

What we would like:
- A Poster (that can be placed in our staff lunch rooms)
- The values to be lined up Horizontally
- Image on the top of the words
- Wording does not all need to be the same text font
- No image photographs - please use image graphics
- No images with people
- No dental related graphics

Target audience: Brivenor staff

Our Values are:
Think Big
Have a go, learn and adapt
If you're gonna do it, do it bloody well
Empower Others
Be a good human

I have uploaded some examples.

Target Market(s)

Brivenor Team members

Industry/Entity Type

Healthcare

Colors

Designer to choose colors to be used in the design.

Requirements
Must have
• Clear horizontal layout, space between each value
Should not have
• No images with humans or dental

```html
<!DOCTYPE html>
<html lang="en">
<head>
<meta charset="utf-8">
<title>Brivenor Australia – Company Values</title>
<link rel="stylesheet" href="https://fonts.googleapis.com/css2?family=Lilita+One&family=Titan+One&family=Anton&family=Oswald:wght@200&family=Montserrat:wght@400;500;600&display=swap">
<style>
  :root {
    --page: #ffffff;
    --navy: #12037f;
    --sky: #1e9ff2;
    --orange: #ff9e00;
    --rust: #c53d00;
    --violet: #7203d9;
    --lilac: #d9c6ff;
    --pink: #ff0057;
    --blush: #ffbcd0;
    --lime: #8ceb00;
    --forest: #1b6f12;
    --white: #ffffff;
  }
  * { box-sizing: border-box; margin: 0; padding: 0; }
  html, body { width: 1200px; height: 848px; overflow: hidden; background: var(--page); }
  .poster {
    position: absolute; left: 54px; top: 232px;
    width: 1084px; height: 373px;
    display: flex;
  }
  .value {
    flex: 1 1 0;
    position: relative;
    overflow: hidden;
    display: flex; flex-direction: column; align-items: center;
    text-align: center;
    text-transform: uppercase;
  }
  .value__icon {
    width: 150px; height: 140px; margin-top: 22px;
    border-radius: 22px;
  }
  .value__words {
    position: absolute; top: 190px; left: 0; right: 0;
    display: flex; flex-direction: column; align-items: center;
    font-weight: 400;
  }
  .value__words span { display: block; white-space: nowrap; }

  /* Think big */
  .value--think { background: var(--navy); }
  .value--think .value__icon { background: radial-gradient(circle, var(--white) 0 38%, var(--sky) 40% 60%, transparent 62%); }
  .think__lead { font: 52px/1 "Lilita One", sans-serif; color: var(--sky); letter-spacing: 1px; }
  .think__main { font: 98px/0.95 "Lilita One", sans-serif; color: var(--white); margin-top: 2px; }

  /* Have a go */
  .value--adapt { background: var(--orange); }
  .value--adapt .value__icon { background: linear-gradient(135deg, var(--rust) 0 50%, var(--white) 50% 100%); opacity: .9; }
  .adapt__lead { font: 29px/1.25 "Titan One", sans-serif; color: var(--rust); }
  .adapt__mid { font: 31px/1.2 "Titan One", sans-serif; color: var(--rust); }
  .adapt__main { font: 48px/1.1 "Titan One", sans-serif; color: var(--white); }

  /* Do it well */
  .value--well { background: var(--violet); }
  .value--well .value__icon { background: radial-gradient(circle at 58% 40%, var(--lilac) 0 30%, var(--white) 31% 40%, var(--lilac) 41% 100%); opacity: .85; }
  .well__lead { font: 400 33px/1.1 "Montserrat", sans-serif; color: var(--lilac); }
  .well__small { font: 15px/1.6 "Titan One", sans-serif; color: var(--lilac); }
  .well__mid { font: 38px/1.05 "Titan One", sans-serif; color: var(--white); }
  .well__main { font: 54px/1 "Titan One", sans-serif; color: var(--white); }

  /* Empower others */
  .value--empower { background: var(--pink); }
  .value--empower .value__icon { background: var(--blush); }
  .empower__main { font: 82px/1 "Anton", sans-serif; color: var(--white); transform: scaleX(.5); margin-top: -4px; }
  .empower__sub { font: 200 80px/1 "Oswald", sans-serif; color: var(--blush); transform: scaleX(.72); margin-top: -2px; }

  /* Good human */
  .value--human { background: var(--lime); }
  .value--human .value__icon { background: linear-gradient(180deg, var(--forest) 0 50%, var(--white) 50% 100%); }
  .human__lead { font: 500 56px/1.05 "Montserrat", sans-serif; color: var(--forest); }
  .human__main { font: 50px/1.1 "Titan One", sans-serif; color: var(--white); }
  .human__sub { font: 600 33px/1.1 "Montserrat", sans-serif; color: var(--forest); }
</style>
</head>
<body>
  <main class="poster" aria-label="Brivenor Australia company values">
    <section class="value value--think">
      <div class="value__icon" role="img" aria-label="Brain shaped as a lightbulb with spark lines"></div>
      <h2 class="value__words"><span class="think__lead">Think</span><span class="think__main">Big</span></h2>
    </section>
    <section class="value value--adapt">
      <div class="value__icon" role="img" aria-label="Paper plane turning into a jet aeroplane"></div>
      <h2 class="value__words"><span class="adapt__lead">Have a go,</span><span class="adapt__mid">Learn &amp;</span><span class="adapt__main">Adapt</span></h2>
    </section>
    <section class="value value--well">
      <div class="value__icon" role="img" aria-label="Magnifying glass over a stack of square tiles"></div>
      <h2 class="value__words"><span class="well__lead">If you're</span><span class="well__small">gonna do it, do it</span><span class="well__mid">Bloody</span><span class="well__main">Well</span></h2>
    </section>
    <section class="value value--empower">
      <div class="value__icon" role="img" aria-label="Four hands joined in a supportive square"></div>
      <h2 class="value__words"><span class="empower__main">Empower</span><span class="empower__sub">Others</span></h2>
    </section>
    <section class="value value--human">
      <div class="value__icon" role="img" aria-label="Open hand holding a young sprouting plant"></div>
      <h2 class="value__words"><span class="human__lead">Be a</span><span class="human__main">Good</span><span class="human__sub">Human</span></h2>
    </section>
  </main>
</body>
</html>
```